Letterhead and Business Cards
Bookkeeping Business
Professional
Marcus J Penhallow
Business Advisor
627 Ravenel Avenue - Suite 100
Bakersfield, CA 93418
Marcus@KRLedgerworks.example
www.KRLedgerworks.example
I will upload the logo that I would like to use on my business card in AI format
Would like to include the Fiscal e-lodge logo and the Certified TallyMint LedgerGuide logo on the back of my card.
Also - reference to the following:
Monthly bookkeeping with financial statement preparation
Individual, corporate & partnership taxes
Payroll services
Business consulting

```html
<!DOCTYPE html>
<html lang="en">
<head>
<meta charset="utf-8">
<title>KRLedger Stationery Concepts</title>
<link href="https://fonts.googleapis.com/css2?family=Open+Sans:wght@400;600;700&display=swap" rel="stylesheet">
<style>
  :root{
    --bg-top:#f3f1ec;
    --bg-bottom:#e6e1d7;
    --paper:#ffffff;
    --navy:#1f3f73;
    --blue:#2f6db3;
    --blue-light:#8fb3dc;
    --green:#4c9a3a;
    --green-dark:#2f7a2a;
    --ink:#5a6270;
    --label:#8a8478;
    --faint:#e3ebf4;
  }
  *{margin:0;padding:0;box-sizing:border-box}
  html,body{width:1200px;height:446px;overflow:hidden}
  body{
    font-family:"Open Sans",Arial,sans-serif;
    background:linear-gradient(180deg,var(--bg-top),var(--bg-bottom));
    position:relative;color:var(--ink);
  }
  .sheet{position:absolute;background:var(--paper);box-shadow:0 2px 6px rgba(0,0,0,.18);overflow:hidden}
  .caption{position:absolute;font-size:7px;letter-spacing:.6px;text-transform:uppercase;color:var(--label)}
  .brand{display:flex;align-items:center;gap:4px;color:var(--navy);font-weight:700;white-space:nowrap}
  .brand-mark{background:var(--blue);flex:none}
  .tagline{font-size:4px;color:var(--blue);letter-spacing:.4px;text-transform:uppercase}
  .tiny{font-size:3.4px;line-height:1.4;color:var(--ink)}

  /* business cards */
  .card{width:120px;height:66px;border-radius:3px}
  .card-front{left:24px;top:132px}
  .card-back{left:24px;top:222px}
  .card .edge{position:absolute;left:0;top:0;bottom:0;width:5px;background:linear-gradient(180deg,var(--navy),var(--blue))}
  .card-front .brand{position:absolute;left:14px;top:14px;font-size:10px}
  .card-front .brand-mark{width:8px;height:8px}
  .card-front .tagline{position:absolute;left:26px;top:27px}
  .card-front .tiny{position:absolute;left:14px;top:38px}
  .card-back .brand{position:absolute;left:14px;top:8px;font-size:9px}
  .card-back .brand-mark{width:7px;height:7px}
  .card-back .tiny{position:absolute;left:14px;top:22px}
  .card-back .badges{position:absolute;right:10px;bottom:8px;display:flex;gap:4px}
  .badge{width:14px;height:10px;background:var(--faint);border:1px solid var(--blue-light)}

  /* letterheads */
  .letterhead{top:22px;width:238px;height:398px}
  .letterhead-one{left:162px}
  .letterhead-two{left:424px;width:300px}
  .letterhead .edge{position:absolute;left:0;top:0;bottom:0;width:7px;background:linear-gradient(180deg,var(--navy),var(--blue),var(--blue-light))}
  .letterhead .brand{position:absolute;left:20px;top:16px;font-size:11px}
  .letterhead .brand-mark{width:9px;height:9px}
  .letterhead .tagline{position:absolute;left:33px;top:30px}
  .letterhead .contact{position:absolute;right:18px;top:17px;text-align:left}
  .letterhead .footer{position:absolute;left:0;right:0;bottom:14px;text-align:center}
  .letterhead-two .contact{display:none}
  .watermark{position:absolute;left:50%;top:52%;transform:translate(-50%,-50%);display:flex;align-items:center;gap:10px;color:var(--faint);font-weight:700;font-size:30px;white-space:nowrap}
  .watermark .brand-mark{width:30px;height:30px;background:var(--faint)}
  .letterhead-one .watermark{font-size:26px}

  /* envelopes */
  .envelope{left:758px;width:430px}
  .env-back{top:22px;height:80px}
  .env-green{top:118px;height:96px;background:var(--green)}
  .env-green .lining{position:absolute;inset:0;background:linear-gradient(160deg,var(--green-dark),var(--green) 60%,#7cbd5e)}
  .env-logo{top:226px;height:64px}
  .env-front{top:300px;height:106px}
  .envelope svg{position:absolute;inset:0}
  .env-logo .brand{position:absolute;left:50%;top:50%;transform:translate(-50%,-50%);font-size:9px}
  .env-logo .brand-mark{width:7px;height:7px}
  .env-front .brand{position:absolute;left:14px;top:12px;font-size:9px}
  .env-front .brand-mark{width:7px;height:7px}
  .env-front .tiny{position:absolute;left:14px;top:26px}
  .env-front .watermark{left:auto;right:20px;top:auto;bottom:10px;transform:none;font-size:22px}
  .env-front .watermark .brand-mark{width:22px;height:22px}
</style>
</head>
<body>

  <div class="caption" style="left:24px;top:120px">Stationery Concepts</div>

  <section class="sheet card card-front">
    <div class="edge"></div>
    <div class="brand"><span class="brand-mark"></span>KRLedger</div>
    <div class="tagline">Bookkeeping Services</div>
    <div class="tiny">Marcus J Penhallow · Business Advisor<br>627 Ravenel Avenue - Suite 100<br>Bakersfield, CA 93418<br>Marcus@KRLedgerworks.example</div>
  </section>
  <div class="caption" style="left:24px;top:202px">Business Card Front</div>

  <section class="sheet card card-back">
    <div class="edge"></div>
    <div class="brand"><span class="brand-mark"></span>KRLedger</div>
    <div class="tiny">Monthly bookkeeping &amp; financial statements<br>Individual, corporate &amp; partnership taxes<br>Payroll services<br>Business consulting</div>
    <div class="badges"><span class="badge"></span><span class="badge"></span></div>
  </section>
  <div class="caption" style="left:24px;top:292px">Business Card Back</div>

  <section class="sheet letterhead letterhead-one">
    <div class="edge"></div>
    <div class="brand"><span class="brand-mark"></span>KRLedger</div>
    <div class="tagline">Bookkeeping Services</div>
    <div class="tiny contact">Marcus J Penhallow<br>627 Ravenel Avenue - Suite 100<br>Bakersfield, CA 93418<br>www.KRLedgerworks.example</div>
    <div class="watermark"><span class="brand-mark"></span>KRLedger</div>
  </section>
  <div class="caption" style="left:162px;top:430px">Letterhead Option 1</div>

  <section class="sheet letterhead letterhead-two">
    <div class="edge"></div>
    <div class="brand"><span class="brand-mark"></span>KRLedger</div>
    <div class="tagline">Bookkeeping Services</div>
    <div class="watermark"><span class="brand-mark"></span>KRLedger</div>
    <div class="tiny footer">627 Ravenel Avenue - Suite 100 · Bakersfield, CA 93418 · Marcus@KRLedgerworks.example · www.KRLedgerworks.example</div>
  </section>
  <div class="caption" style="left:424px;top:430px">Letterhead Option 2</div>

  <section class="sheet envelope env-back">
    <svg width="430" height="80" viewBox="0 0 430 80"><path d="M0 0 L215 44 L430 0" fill="none" stroke="#d9dde3" stroke-width="1"/><path d="M0 80 L170 36 M430 80 L260 36" stroke="#e6e9ee" stroke-width="1"/></svg>
  </section>

  <section class="sheet envelope env-green">
    <div class="lining"></div>
    <svg width="430" height="96" viewBox="0 0 430 96"><path d="M0 40 L215 82 L430 40 L430 96 L0 96 Z" fill="#ffffff"/><path d="M0 40 L215 82 L430 40" fill="none" stroke="#d9dde3" stroke-width="1"/></svg>
  </section>

  <section class="sheet envelope env-logo">
    <svg width="430" height="64" viewBox="0 0 430 64"><path d="M0 0 L215 40 L430 0" fill="none" stroke="#d9dde3" stroke-width="1"/></svg>
    <div class="brand"><span class="brand-mark"></span>KRLedger</div>
  </section>

  <section class="sheet envelope env-front">
    <div class="brand"><span class="brand-mark"></span>KRLedger</div>
    <div class="tiny">627 Ravenel Avenue - Suite 100<br>Bakersfield, CA 93418</div>
    <div class="watermark"><span class="brand-mark"></span>KRLedger</div>
  </section>
  <div class="caption" style="left:758px;top:430px">Envelope Option 3</div>

</body>
</html>
```